Training Company Needs a Web Design

We are a Training company that needs a website design completed for us. "The Harbor Loft" The website will be a 'community space' specialising in 'Change and Transformation'. It will be a 'space' where individuals can come to find out 'latest news', upcoming events and courses, chat with others and find 'tools and templates'. They will need to login as a 'Member'.

The final design needs to be professional but have a 'fun and interactive' feel and appeal to our target audience who are predominantly corporate individuals.

Target Market(s)

Corporate Individuals - they may have a Change or Project background

Industry/Entity Type

Business Consultant

Number of Pages Required

3 page

Font styles to use
Sans Serif

Requirements
Must have
• Design for 'Home Page'
• A professional and corporate 'feel' but be fun and interactive.
Nice to have
• A 'sense' of how some of the other pages may be designed or laid out.

```html
<!DOCTYPE html>
<html lang="en">
<head>
<meta charset="utf-8">
<title>The Harbor Loft — Home</title>
<link href="https://fonts.googleapis.com/css2?family=Open+Sans:wght@400;600;700&family=Roboto+Condensed:wght@300;400;700&display=swap" rel="stylesheet">
<style>
:root{
  --blue:#0b82c4;
  --blue-dark:#06679f;
  --ink:#333333;
  --text:#555555;
  --grey-band:#e4e4e4;
  --white:#ffffff;
  --footer:#141414;
  --footer-line:#2c2c2c;
  --teal:#54d3c4;
  --ocean:#1e6aa8;
}
*{box-sizing:border-box;margin:0;padding:0}
html,body{width:1200px;height:3550px;overflow:hidden}
body{font-family:"Open Sans",Arial,sans-serif;color:var(--text);background:var(--white);position:relative}
.heading{font-family:"Roboto Condensed","Arial Narrow",sans-serif;font-weight:400;color:var(--ink)}
.accent{color:var(--blue)}
p{font-size:15px;line-height:25px}

/* hero */
.hero{position:absolute;left:0;top:0;width:1200px;height:710px;
  background:linear-gradient(135deg,#c9d6e2 0%,#e9eef3 40%,#b7c6d6 75%,#8fa3b8 100%)}
.brand{position:absolute;left:400px;top:245px;display:flex;align-items:center;gap:24px}
.brand-mark{width:64px;height:64px;border-radius:50%;background:var(--blue)}
.brand-name{font-family:"Roboto Condensed","Arial Narrow",sans-serif;font-weight:300;font-size:66px;line-height:72px;color:var(--blue-dark);letter-spacing:1px}

/* navigation */
.main-nav{position:absolute;left:0;top:710px;width:1200px;height:64px;background:var(--blue);display:flex;padding-left:163px}
.main-nav a{font-family:"Roboto Condensed","Arial Narrow",sans-serif;font-size:17px;color:var(--white);text-decoration:none;height:64px;line-height:64px;padding:0 36px}
.main-nav a.active{background:var(--blue-dark)}

/* welcome */
.welcome{position:absolute;left:0;top:774px;width:1200px;height:315px;text-align:center}
.welcome h1{font-size:54px;margin-top:50px;line-height:62px}
.welcome p{width:850px;margin:14px auto 0}
.btn-outline{display:inline-block;margin-top:20px;width:176px;height:50px;line-height:48px;border:2px solid var(--blue);color:var(--blue);font-family:"Roboto Condensed","Arial Narrow",sans-serif;font-size:19px}

/* feature rows */
.feature{position:absolute;left:0;width:1200px}
.feature.training{top:1089px;height:414px;background:var(--grey-band)}
.feature.coaching{top:1503px;height:433px;background:var(--white)}
.feature h2{font-size:52px;line-height:60px;color:var(--blue);position:absolute}
.feature .copy{position:absolute;width:460px}
.feature .copy p+p{margin-top:25px}
.photo{position:absolute}
.training h2{left:78px;top:50px}
.training .copy{left:78px;top:120px}
.training .photo{left:601px;top:50px;width:502px;height:295px;background:linear-gradient(120deg,#e7edf2,#b9c7d3 60%,#8d9eb0)}
.coaching h2{left:634px;top:60px}
.coaching .copy{left:634px;top:125px}
.coaching .photo{left:78px;top:76px;width:497px;height:296px;background:linear-gradient(120deg,#9aa7b2,#dfe5ea 50%,#5e6a77)}

/* courses */
.courses{position:absolute;left:0;top:1936px;width:1200px;height:431px;background:linear-gradient(100deg,var(--teal) 0%,#2f9dbb 45%,var(--ocean) 100%);text-align:center;color:var(--white)}
.courses h2{color:var(--white);font-size:52px;line-height:60px;margin-top:50px}
.course-list{display:flex;justify-content:center;gap:60px;margin-top:42px}
.course{width:305px}
.course svg{display:block;margin:0 auto;height:60px}
.course h3{font-family:"Roboto Condensed","Arial Narrow",sans-serif;font-weight:400;font-size:25px;margin-top:12px}
.course p{margin-top:12px;color:#eef7fb}

/* news */
.news{position:absolute;left:0;top:2367px;width:1200px;height:438px}
.news h2{text-align:center;font-size:52px;line-height:60px;margin-top:46px}
.news-list{position:absolute;left:78px;top:118px;display:flex;gap:54px}
.news-card{width:313px}
.news-card .photo{position:static;width:313px;height:154px}
.news-card h3{font-size:16px;font-weight:600;color:var(--blue);margin-top:14px}
.news-card p{margin-top:4px;color:var(--ink)}
.read-more{display:block;font-size:14px;font-weight:700;color:#111;margin-top:6px;text-decoration:none}

/* events */
.events{position:absolute;left:0;top:2805px;width:1200px;height:256px;background:var(--grey-band)}
.events h2{text-align:center;font-size:52px;line-height:60px;margin-top:48px}
.event-list{position:absolute;left:78px;top:123px;display:flex;gap:78px}
.event{display:flex;gap:18px;width:289px}
.date{width:81px;flex:none;text-align:center}
.date .day{background:var(--blue);color:var(--white);font-family:"Roboto Condensed","Arial Narrow",sans-serif;font-weight:700;font-size:36px;height:50px;line-height:50px}
.date .month{background:var(--white);font-size:15px;height:28px;line-height:28px;color:var(--text)}
.event p{color:var(--text);line-height:23px}
.event .read-more{color:var(--blue);margin-top:2px}

/* partners */
.partners{position:absolute;left:0;top:3061px;width:1200px;height:153px}
.badge{position:absolute;background:#cfd6dc;border-radius:4px}

/* footer */
.site-footer{position:absolute;left:0;top:3214px;width:1200px;height:336px;background:var(--footer);color:var(--white)}
.footer-col{position:absolute;top:36px;width:330px}
.footer-col h4{font-family:"Roboto Condensed","Arial Narrow",sans-serif;font-weight:400;font-size:24px}
.links{list-style:none;margin-top:10px}
.links li{font-size:15px;line-height:31px}
.links li::before{content:"\2192";margin-right:8px}
.links li.current{color:var(--blue)}
.footer-col p{margin-top:12px;color:#eee}
.field{width:310px;height:36px;border:1px solid #bbb;margin-top:20px;padding-left:8px;font-size:14px;line-height:34px;color:#ddd}
.field+.field{margin-top:18px}
.btn-login{margin-top:18px;width:125px;height:36px;background:var(--white);color:var(--blue);font-family:"Roboto Condensed","Arial Narrow",sans-serif;font-size:19px;text-align:center;line-height:36px}
.contact-row{display:flex;gap:12px;margin-top:12px;font-size:15px;line-height:25px;color:#eee}
.contact-row svg{flex:none;margin-top:4px}
.social{display:flex;gap:22px;margin-top:18px}
.social span{width:56px;height:56px;border-radius:50%;border:2px solid var(--white)}
.social span.filled{background:var(--blue);border-color:var(--blue)}
.copyright{position:absolute;left:0;bottom:0;width:1200px;height:46px;border-top:1px solid var(--footer-line);text-align:center;font-size:15px;line-height:46px}
.copyright b{color:var(--blue)}
</style>
</head>
<body>

<header class="hero" role="img" aria-label="Photo of two businessmen reviewing a tablet together">
  <div class="brand"><span class="brand-mark"></span><span class="brand-name">THE HARBOR LOFT</span></div>
</header>

<nav class="main-nav">
  <a class="active">HOME</a><a>ABOUT</a><a>TRAINING</a><a>COURSES</a><a>NEWS</a><a>EVENT</a><a>CONTACT</a>
</nav>

<section class="welcome">
  <h1 class="heading">Welcome to <span class="accent">The Harbor Loft</span></h1>
  <p>Lorem Ipsum is simply dummy text of the printing and typesetting industry. Lorem Ipsum has been the industry's standard dummy text ever since the 1500s, when an unknown printer took a galley of type and scrambled it to make a type specimen book.</p>
  <span class="btn-outline">READ MORE</span>
</section>

<section class="feature training">
  <h2 class="heading">Training</h2>
  <div class="copy">
    <p>Lorem Ipsum is simply dummy text of the printing and typesetting industry. Lorem Ipsum has been the industry's standard dummy text ever since the 1500s, when an unknown printer took a galley of type and scrambled it to make a type specimen book.</p>
    <p>Lorem Ipsum is simply dummy text of the printing and typesetting industry. Lorem Ipsum has been the industry's standard dummy text ever since the 1500.</p>
  </div>
  <div class="photo" role="img" aria-label="Photo of a trainer presenting at a whiteboard to a seated group"></div>
</section>

<section class="feature coaching">
  <div class="photo" role="img" aria-label="Photo of a business team meeting around a conference table"></div>
  <h2 class="heading">Coaching</h2>
  <div class="copy">
    <p>Lorem Ipsum is simply dummy text of the printing and typesetting industry. Lorem Ipsum has been the industry's standard dummy text ever since the 1500s, when an unknown printer took a galley of type and scrambled it to make a type specimen book.</p>
    <p>Lorem Ipsum is simply dummy text of the printing and typesetting industry. Lorem Ipsum has been the industry's standard dummy text ever since the 1500.</p>
  </div>
</section>

<section class="courses">
  <h2 class="heading">Courses</h2>
  <div class="course-list">
    <div class="course">
      <svg viewBox="0 0 60 60" width="60" aria-hidden="true"><g stroke="#fff" stroke-width="3"><line x1="30" y1="30" x2="10" y2="10"/><line x1="30" y1="30" x2="50" y2="10"/><line x1="30" y1="30" x2="10" y2="50"/><line x1="30" y1="30" x2="50" y2="50"/></g><g fill="#fff"><circle cx="30" cy="30" r="9"/><circle cx="10" cy="10" r="6"/><circle cx="50" cy="10" r="6"/><circle cx="10" cy="50" r="6"/><circle cx="50" cy="50" r="6"/></g></svg>
      <h3>Course Name</h3>
      <p>Lorem Ipsum is simply dummy text of the printing and typesetting industry. Lorem Ipsum has been the industry.</p>
    </div>
    <div class="course">
      <svg viewBox="0 0 60 60" width="60" aria-hidden="true"><path d="M16 6h34v40H20a6 6 0 0 0 0 12h30" fill="none" stroke="#fff" stroke-width="4"/><path d="M16 6h34v40H16z" fill="#fff"/><g stroke="#2f9dbb" stroke-width="2"><line x1="24" y1="16" x2="44" y2="16"/><line x1="24" y1="24" x2="44" y2="24"/></g></svg>
      <h3>Course Name</h3>
      <p>Lorem Ipsum is simply dummy text of the printing and typesetting industry. Lorem Ipsum has been the industry.</p>
    </div>
    <div class="course">
      <svg viewBox="0 0 60 60" width="60" aria-hidden="true"><g fill="#fff"><circle cx="30" cy="16" r="10"/><path d="M12 50c0-12 8-20 18-20s18 8 18 20z"/><rect x="4" y="50" width="52" height="5" rx="2"/></g></svg>
      <h3>Course Name</h3>
      <p>Lorem Ipsum is simply dummy text of the printing and typesetting industry. Lorem Ipsum has been the industry.</p>
    </div>
  </div>
</section>

<section class="news">
  <h2 class="heading">Latest <span class="accent">News</span></h2>
  <div class="news-list">
    <article class="news-card">
      <div class="photo" role="img" aria-label="Photo of a smiling office team gathered at a desk" style="background:linear-gradient(120deg,#f0ece6,#c9b8a6 55%,#8b97a3)"></div>
      <h3>Lorem Ipsum is simply dummy text.</h3>
      <p>Lorem Ipsum is simply dummy text of the printing and typesetting industry.</p>
      <a class="read-more">READ MORE</a>
    </article>
    <article class="news-card">
      <div class="photo" role="img" aria-label="Photo of a woman sitting cross-legged with a laptop" style="background:linear-gradient(120deg,#c6cfdc,#a9b5c8 55%,#8e9cb4)"></div>
      <h3>Lorem Ipsum is simply dummy text.</h3>
      <p>Lorem Ipsum is simply dummy text of the printing and typesetting industry.</p>
      <a class="read-more">READ MORE</a>
    </article>
    <article class="news-card">
      <div class="photo" role="img" aria-label="Photo of businessmen in suits discussing documents" style="background:linear-gradient(120deg,#dfe6ee,#6d83a0 55%,#2e3f5a)"></div>
      <h3>Lorem Ipsum is simply dummy text.</h3>
      <p>Lorem Ipsum is simply dummy text of the printing and typesetting industry.</p>
      <a class="read-more">READ MORE</a>
    </article>
  </div>
</section>

<section class="events">
  <h2 class="heading">Upcoming <span class="accent">Event</span></h2>
  <div class="event-list">
    <div class="event"><div class="date"><div class="day">24</div><div class="month">Feb</div></div><div><p>Lorem Ipsum is simply dummy text of the printing</p><a class="read-more">READ MORE</a></div></div>
    <div class="event"><div class="date"><div class="day">26</div><div class="month">Feb</div></div><div><p>Lorem Ipsum is simply dummy text of the printing</p><a class="read-more">READ MORE</a></div></div>
    <div class="event"><div class="date"><div class="day">27</div><div class="month">Feb</div></div><div><p>Lorem Ipsum is simply dummy text of the printing</p><a class="read-more">READ MORE</a></div></div>
  </div>
</section>

<section class="partners" aria-label="Partner badges">
  <span class="badge" style="left:160px;top:44px;width:136px;height:64px"></span>
  <span class="badge" style="left:404px;top:52px;width:130px;height:46px"></span>
  <span class="badge" style="left:630px;top:38px;width:128px;height:78px"></span>
  <span class="badge" style="left:858px;top:46px;width:134px;height:58px"></span>
</section>

<footer class="site-footer">
  <div class="footer-col" style="left:78px">
    <h4>Useful Links</h4>
    <ul class="links">
      <li class="current">Home</li><li>About</li><li>Training</li><li>Courses</li><li>News</li><li>Event</li><li>Contact</li>
    </ul>
  </div>
  <div class="footer-col" style="left:445px">
    <h4>Login</h4>
    <p>Lorem Ipsum is simply dummy text of the printing and typesetting industry.</p>
    <div class="field">Enter Email</div>
    <div class="field">Enter Password</div>
    <div class="btn-login">LOGIN</div>
  </div>
  <div class="footer-col" style="left:812px">
    <h4>Get In Touch With Us</h4>
    <div class="contact-row"><svg width="16" height="20" viewBox="0 0 16 20" aria-hidden="true"><path d="M8 0a7 7 0 0 0-7 7c0 5 7 13 7 13s7-8 7-13a7 7 0 0 0-7-7zm0 10a3 3 0 1 1 0-6 3 3 0 0 1 0 6z" fill="#fff"/></svg><span>Lorem Ipsum is simply dummy text of the printing and typesetting industry.</span></div>
    <div class="contact-row"><svg width="16" height="16" viewBox="0 0 16 16" aria-hidden="true"><path d="M3 0l3 4-2 2c1 2 4 5 6 6l2-2 4 3-2 3C7 16 0 9 0 3z" fill="#fff"/></svg><span>123 456 7890</span></div>
    <div class="contact-row"><svg width="18" height="14" viewBox="0 0 18 14" aria-hidden="true"><rect x="1" y="1" width="16" height="12" fill="none" stroke="#fff" stroke-width="2"/><path d="M1 1l8 7 8-7" fill="none" stroke="#fff" stroke-width="2"/></svg><span>info@harborloftmail.com</span></div>
    <div class="social"><span class="filled"></span><span></span><span></span></div>
  </div>
  <div class="copyright">© <b>THE HARBOR LOFT</b> - 2016. All Rights Reserved.</div>
</footer>

</body>
</html>
```